Drinking and Driving course for the courts

Sophisitcated tri-fold brochure seen by judges, lawyers etc. People taking this course have been charged with drinking and driving (alcohol). Should be classy and upmarket. Please be creative like original brochure. Please use exact wording and in same order as brochure. Also please keep in approximately same place on brochure. Spelling and grammar should be exactly same as this document is already proof-read and checked by experts.

Target Market(s)

Judges, lawyers, court system.

Industry/Entity Type

Legal

Font styles to use
Serif

Requirements
Must have
• Creative and classy. Can look similar or same as original brochure. Should have pciture/graphic of car keys and drink
Nice to have
• A background graphic like in original brochure comes across very well. Subtle etc.
Should not have
• Does not need to have pictures of vehicles/cars. Definitely no brand names of cars or alcohol labels (or any kind).

```html
<!DOCTYPE html>
<html lang="en">
<head>
<meta charset="utf-8">
<title>Clear Course – Tri-fold Brochure</title>
<link href="https://fonts.googleapis.com/css2?family=Montserrat:ital,wght@0,400;0,500;0,600;0,700;1,300&display=swap" rel="stylesheet">
<style>
  :root{
    --navy:#2f4b7c;
    --ink:#2a2a2a;
    --body:#3d3d3d;
    --paper:#ffffff;
    --canvas:#e9eaec;
    --on-navy:#e6ebf4;
  }
  *{box-sizing:border-box;margin:0;padding:0}
  html,body{width:1200px;height:3000px;overflow:hidden;background:var(--canvas);font-family:'Montserrat',Arial,sans-serif;color:var(--body)}
  .spread{position:absolute;left:60px;width:1080px;height:762px;display:flex;background:var(--paper);box-shadow:0 10px 26px rgba(0,0,0,.22)}
  .spread--inside{top:620px}
  .spread--outside{top:1560px}
  .panel{width:360px;height:100%;position:relative;padding:46px 40px 40px 48px}
  .panel--navy{background:var(--navy);color:#fff}
  .h-section{font-weight:600;color:var(--navy);font-size:22px;line-height:1.15;margin-bottom:8px}
  .lede{font-weight:700;font-size:11.5px;line-height:1.35;color:var(--ink);margin-bottom:14px}
  .sub{font-weight:700;font-size:11.5px;line-height:1.35;color:var(--ink);margin:6px 0 10px}
  .steps{list-style:none;position:relative;margin-bottom:24px}
  .steps::before{content:"";position:absolute;left:10px;top:8px;bottom:10px;width:1.5px;background:var(--navy)}
  .steps li{position:relative;padding-left:30px;font-size:10.5px;line-height:1.35;margin-bottom:10px}
  .num{position:absolute;left:0;top:-2px;width:21px;height:21px;border-radius:50%;background:var(--navy);color:#fff;font-size:9.5px;font-weight:700;display:flex;align-items:center;justify-content:center}
  .panel--navy .steps::before{background:rgba(255,255,255,.7)}
  .panel--navy .num{background:#fff;color:var(--navy)}
  .panel--navy .steps li{color:var(--on-navy)}
  .costs p{font-size:10.5px;line-height:1.4;margin-bottom:14px}
  .intro{font-size:10.5px;line-height:1.35;color:var(--on-navy);margin-bottom:18px}
  .nav-head{font-weight:700;font-size:12px;line-height:1.3;margin-bottom:10px}
  .photo--glasses{width:268px;height:156px;margin:8px 0 22px;border-radius:8px;border:3px solid #fff;background:linear-gradient(135deg,#d9d4c4,#a89363 45%,#6c6a63)}
  .one-on-one{font-weight:600;font-size:22px;line-height:1.25;letter-spacing:.5px}
  .remote{font-weight:600;color:var(--navy);font-size:22px;letter-spacing:.5px;text-align:center}
  .laptop{width:250px;height:168px;margin:28px auto 26px;border-radius:6px;background:linear-gradient(180deg,#f2f3f6,#d5d9e2)}
  .cost{text-align:center;color:var(--ink)}
  .cost strong{display:block;font-weight:500;font-size:24px}
  .cost span{font-size:23px}
  .course-name{font-weight:700;color:var(--navy);font-size:44px;line-height:1.05;text-align:center;margin:34px 0 24px}
  .school{text-align:center}
  .school-name{font-weight:700;color:var(--navy);font-size:16px;display:flex;align-items:center;justify-content:center;gap:8px}
  .school-name .dot{width:10px;height:10px;border-radius:50%;background:var(--navy)}
  .tagline{font-size:9.5px;font-weight:600;color:var(--navy);margin:8px 0 12px}
  .rule{height:2px;background:var(--navy);width:210px;margin:0 auto 14px;opacity:.8}
  .needs{font-size:9.5px;font-weight:600;color:var(--navy);line-height:1.4}
  .bg-list li{font-size:10.2px;text-align:justify;margin-bottom:16px}
  .bg-list li b{color:var(--navy);font-weight:700}
  .slogan{font-style:italic;font-weight:300;font-size:32px;line-height:1.3;text-align:center;margin-top:12px}
  .more{font-weight:600;font-size:21px;text-align:center;margin:70px 0 22px}
  .contact-stack{text-align:center}
  .icon-ring{width:30px;height:30px;border:1.5px solid #fff;border-radius:50%;display:flex;align-items:center;justify-content:center;margin:0 auto 8px}
  .phone-big{font-weight:600;font-size:23px;letter-spacing:1px;margin-bottom:22px}
  .contact-line{font-size:11.5px;font-weight:600;margin-bottom:20px}
  .panel--cover{padding:0}
  .cover-photo{position:absolute;left:0;top:0;width:100%;height:300px;background:linear-gradient(180deg,#f4f4f2 0%,#e6e4df 50%,#b9a588 80%,#9c8a70 100%)}
  .panel--cover .course-name{position:relative;margin:34px 0 0}
  .frame{position:absolute;left:28px;right:28px;top:318px;border:2px solid var(--navy);border-radius:10px;padding:22px 10px 20px}
  .cover-contacts{position:absolute;left:40px;top:500px}
  .cover-contacts div{display:flex;align-items:center;gap:8px;font-size:11px;font-weight:600;color:var(--ink);margin-bottom:10px}
  .cover-contacts .phone{font-size:22px;letter-spacing:.5px}
</style>
</head>
<body>

<section class="spread spread--inside">
  <div class="panel">
    <h2 class="h-section">Clear Course...</h2>
    <p class="lede">A 1-day, 7-hour, intensive remedial measures course for those charged with being under the influence of alcohol.</p>
    <p class="lede">Our goal is to equip our customers with knowledge and help them to avoid something devastating and/or irreversible from happening in the</p>
    <h2 class="h-section">During the course<br>we will:</h2>
    <p class="sub">Look at how alcohol<br>affects us from a physical standpoint:</p>
    <ul class="steps">
      <li><span class="num">01</span>What is a serving of alcohol?</li>
      <li><span class="num">02</span>Blood alcohol concentration (BAC) and the many factors that go into creating our individual BAC/level of intoxication, how much does it take to get us to 0.05/0.08; how long to wear off?</li>
      <li><span class="num">03</span>Effects on different organs in the body including diabetes, cirrhosis etc.; effects on the brain/cognition at different levels of impairment</li>
    </ul>
    <h2 class="h-section">Count the costs<br>including:</h2>
    <div class="costs">
      <p>Financial: fines, programs fees, court costs, legal fees, insurance</p>
      <p>Human impact: personal relationships, criminal record, job prospects, international travel, custody, physical injury</p>
    </div>
  </div>

  <div class="panel panel--navy">
    <p class="intro">Help you gain a thorough understanding of the laws in Ontario &amp; Canada (the Highway Traffic Act &amp; Criminal Code of Canada)</p>
    <p class="nav-head">Look at the psychology<br>of addiction:</p>
    <ul class="steps">
      <li><span class="num">01</span>Stages of change model (how to improve our habits)</li>
      <li><span class="num">02</span>Define and explore neuroplasticity and the established science behind how we train and can retrain the brain</li>
    </ul>
    <p class="nav-head">Reflective study based on what<br>the night out looks like:</p>
    <ul class="steps">
      <li><span class="num">01</span>Triggers and events leading up to the arrest</li>
      <li><span class="num">02</span>Alternatives--what tangible things can we do differently moving forward?</li>
    </ul>
    <p class="nav-head">Look at how genetics and role models influence our learned behaviours</p>
    <div class="photo--glasses" role="img" aria-label="Photograph of several emptied whisky glasses on a table"></div>
    <p class="one-on-one">COURSES ARE<br>ONE-ON-ONE</p>
  </div>

  <div class="panel">
    <p class="remote">OFFERED REMOTELY!</p>
    <div class="laptop" role="img" aria-label="Illustration of a laptop showing an online video lesson"></div>
    <p class="cost"><strong>Course Cost:</strong><span>$775.00 + HST</span></p>
    <h1 class="course-name">Clear<br>Course</h1>
    <div class="school">
      <p class="school-name"><span class="dot"></span>Lakeline Driving School</p>
      <p class="tagline">Making drivers safe...for life!</p>
      <div class="rule"></div>
      <p class="needs">For all your G License needs!<br>Beginner, Rehabilitation &amp; Remedial</p>
    </div>
  </div>
</section>

<section class="spread spread--outside">
  <div class="panel">
    <h2 class="h-section">Our background:</h2>
    <ul class="steps bg-list">
      <li><span class="num">01</span><b>Since its inception in 1998,</b> Lakeline Driving School has strived to help drivers maintain their driving independence while leading safe and productive lives. Our motto "making drivers safe for life" drives our vision of helping drivers across industries and at all stages of our driving careers.</li>
      <li><span class="num">02</span><b>Lakeline started out working with school boards</b> to deliver driver training to beginner drivers. Thousands of students have graduated from our ministry-approved curriculum throughout central Ontario. We are also ministry-approved to instruct defensive driving <b>(DDC)</b> and driver improvement courses <b>(DIC),</b> for drivers with speeding tickets, demerit points and at fault crashes.</li>
      <li><span class="num">03</span><b>Lakeline has also evolved to provide comprehensive</b> driver rehabilitation to those who have lost, or are at risk of losing their license for medical reasons. This includes mobility issues requiring adaptive equipment, as well as traumatic crashes resulting in cognitive impairments and PTSD. We work with clients before the courts charged with impaired driving (alcohol, cannabis, opioids), road rage and stunt driving.</li>
      <li><span class="num">04</span><b>Founder Daniel Hartley started driving at an early</b> age on his parent's farm. Driving professionally and doing so safely is in his DNA. Daniel graduated from Pinecrest College School, and obtained a degree in Business and Psychology from Northvale University. He is a certified in-car and in-class driving instructor and trainer.</li>
    </ul>
  </div>

  <div class="panel panel--navy">
    <p class="slogan">Maintaining<br>driving<br>independence,<br>while leading<br>safe and<br>productive<br>lives!</p>
    <p class="more">For more information:</p>
    <div class="contact-stack">
      <div class="icon-ring"><svg width="14" height="14" viewBox="0 0 24 24" fill="#fff"><path d="M6.6 10.8a15 15 0 0 0 6.6 6.6l2.2-2.2a1 1 0 0 1 1-.25 11.4 11.4 0 0 0 3.6.57 1 1 0 0 1 1 1V20a1 1 0 0 1-1 1A17 17 0 0 1 3 4a1 1 0 0 1 1-1h3.5a1 1 0 0 1 1 1c0 1.25.2 2.45.57 3.57a1 1 0 0 1-.25 1z"/></svg></div>
      <p class="phone-big">705-555-0148</p>
      <div class="icon-ring"><svg width="14" height="12" viewBox="0 0 24 18" fill="none" stroke="#fff" stroke-width="2"><rect x="1" y="1" width="22" height="16" rx="2"/><path d="M1 2l11 8 11-8"/></svg></div>
      <p class="contact-line">dhartley@lakelinedriving.ca</p>
      <div class="icon-ring"><svg width="15" height="15" viewBox="0 0 24 24" fill="none" stroke="#fff" stroke-width="1.8"><circle cx="12" cy="12" r="10"/><path d="M2 12h20M12 2c3 3 3 17 0 20M12 2c-3 3-3 17 0 20"/></svg></div>
      <p class="contact-line">www.lakelinedriving.ca</p>
    </div>
  </div>

  <div class="panel panel--cover">
    <div class="cover-photo" role="img" aria-label="Photograph of a glass of whisky beside a set of car keys on a wooden table"></div>
    <h1 class="course-name">Clear<br>Course</h1>
    <div class="frame school">
      <p class="school-name"><span class="dot"></span>Lakeline Driving School</p>
      <p class="tagline">Making drivers safe...for life!</p>
      <div class="rule"></div>
      <p class="needs">For all your G License needs!<br>Beginner, Rehabilitation &amp; Remedial</p>
    </div>
    <div class="cover-contacts">
      <div><svg width="12" height="12" viewBox="0 0 24 24" fill="none" stroke="#2a2a2a" stroke-width="2"><circle cx="12" cy="12" r="10"/><path d="M2 12h20M12 2c3 3 3 17 0 20M12 2c-3 3-3 17 0 20"/></svg>www.lakelinedriving.ca</div>
      <div><svg width="12" height="10" viewBox="0 0 24 18" fill="none" stroke="#2a2a2a" stroke-width="2"><rect x="1" y="1" width="22" height="16" rx="2"/><path d="M1 2l11 8 11-8"/></svg>dhartley@lakelinedriving.ca</div>
      <div class="phone"><svg width="16" height="16" viewBox="0 0 24 24" fill="#2a2a2a"><path d="M6.6 10.8a15 15 0 0 0 6.6 6.6l2.2-2.2a1 1 0 0 1 1-.25 11.4 11.4 0 0 0 3.6.57 1 1 0 0 1 1 1V20a1 1 0 0 1-1 1A17 17 0 0 1 3 4a1 1 0 0 1 1-1h3.5a1 1 0 0 1 1 1c0 1.25.2 2.45.57 3.57a1 1 0 0 1-.25 1z"/></svg>705-555-0148</div>
    </div>
  </div>
</section>

</body>
</html>
```